Flyer-Design für Konzertflyer gemischter Chor
Zielgruppe
Wir, die Klangfreunde Wellbach sind ein gemischter Chor aus der Schweiz. Für unser nächstes Konzert mit dem Titel ' Lieder zum Träumen' brauchen wir einen Flyer der auf den Anlass Aufmerksam macht.
Näheres zum Chor auf unserer Website www.klangfreunde-wellbach.ch.
Aufgabenstellung
Mit dem Titel sind nicht nur Lieder zum verlieben gemeint sondern auch Songs in die man sich verlieben kann oder die einem an etwas schönes Erinnern. Wir denken da an ein stimmungsvolles Design mit nicht nur roten Herzen.
Programmausschnitt: Winds across the silver bay , Harlan Moody / Lanterns in the rain / Kima Soro / Walk beside the quiet river tonight, Garth Wells / Paper boats at dusk, Russ Tanner / Tidal hymn, Trevor Halloway / Brightwater, Harbor lane tales / Bells over meadows , Cedar hall
Format: A5 hochkant.
Text: "Lieder zum Träumen" Konzert Klangfreunde Wellbach.
Samstag 19. November 17.00 Uhr, Wellbach/Rosstal, Singsaal Lindenhain
Sonntag 20. November 17.00Uhr, Lindau am Weiher, Kornblumsaal
Eintritt frei Kollekte
www.klangfreunde-wellbach.ch

```html
<!DOCTYPE html>
<html lang="de">
<head>
<meta charset="utf-8">
<title>Lieder zum Träumen – Konzert Klangfreunde Wellbach</title>
<link rel="stylesheet" href="https://fonts.googleapis.com/css2?family=Fira+Sans:ital,wght@1,800;1,900&family=Barlow:wght@500;600;700&display=swap">
<style>
  :root {
    --stage: #d9d9d9;
    --paper: #ffffff;
    --red: #cf1427;
    --magenta: #d1157d;
    --ink: #2b2b2b;
    --photo-light: #cfc6b8;
    --photo-mid: #a89c8a;
    --photo-dark: #6f6354;
  }
  * { margin: 0; padding: 0; box-sizing: border-box; }
  html, body {
    width: 1200px; height: 1200px; overflow: hidden;
    background: var(--stage);
  }
  .flyer {
    position: absolute; left: 220px; top: 50px;
    width: 760px; height: 1100px;
    background: var(--paper);
    overflow: hidden;
    box-shadow: 0 4px 18px rgba(0,0,0,.18);
  }
  .title { font-size: inherit; font-weight: inherit; }
  .headline {
    position: absolute;
    font-family: "Fira Sans", "Arial Black", sans-serif;
    font-style: italic; font-weight: 900;
    color: var(--red);
    line-height: 1;
    white-space: nowrap;
    letter-spacing: -1px;
  }
  .headline--top { left: 54px; top: 20px; font-size: 100px; }
  .headline--small { left: 60px; top: 189px; font-size: 28px; font-weight: 800; letter-spacing: 0; }
  .headline--bottom { left: 150px; top: 133px; font-size: 95px; }
  .tag {
    position: absolute; left: 342px; top: 86px;
    width: 400px; height: 52px;
    background: var(--magenta);
    color: #fff;
    font-family: "Barlow", Arial, sans-serif; font-weight: 700;
    font-size: 25px;
    display: flex; align-items: center; justify-content: center;
    white-space: nowrap;
    transform: rotate(-3deg);
    box-shadow: 0 2px 4px rgba(0,0,0,.2);
  }
  .photo {
    position: absolute; left: 0; top: 240px;
    width: 760px; height: 451px;
    background: radial-gradient(ellipse at 55% 55%, var(--photo-light) 0%, var(--photo-mid) 60%, var(--photo-dark) 100%);
  }
  .badge {
    position: absolute; left: 76px; top: 283px;
    width: 144px; height: 144px; border-radius: 50%;
    background: var(--magenta);
    color: #fff;
    font-family: "Barlow", Arial, sans-serif; font-weight: 700;
    font-size: 19px; line-height: 1.25;
    display: flex; align-items: center; justify-content: center;
    text-align: center;
  }
  .date {
    position: absolute; left: 0; width: 760px; text-align: center;
    font-family: "Fira Sans", "Arial Black", sans-serif;
    font-style: italic; font-weight: 900;
    color: var(--red); line-height: 1;
    white-space: nowrap;
  }
  .date__day { font-size: 58px; margin-right: 10px; }
  .date__num { font-size: 44px; }
  .date--sat { top: 738px; }
  .date--sun { top: 888px; }
  .venue {
    position: absolute; left: 0; width: 760px; text-align: center;
    font-family: "Barlow", Arial, sans-serif; font-weight: 500;
    color: var(--ink); font-size: 23px; line-height: 32px;
  }
  .venue--sat { top: 804px; }
  .venue--sun { top: 954px; }
  .website {
    position: absolute; left: 0; top: 1036px; width: 760px; text-align: center;
    font-family: "Barlow", Arial, sans-serif; font-weight: 700;
    color: var(--ink); font-size: 25px;
  }
</style>
</head>
<body>
  <article class="flyer">
    <div class="photo" role="img" aria-label="Stimmungsvolles Foto: zwei Kinder in Vintage-Kleidung sitzen auf einem alten Koffer vor einer hellen Backsteinwand, rote Herzballone schweben darüber"></div>

    <h1 class="title">
      <span class="headline headline--top">LIEDER</span>
      <span class="headline headline--small">ZUM</span>
      <span class="headline headline--bottom">TRÄUMEN</span>
    </h1>
    <div class="tag">Konzert Klangfreunde Wellbach</div>

    <div class="badge">Eintritt frei –<br>Kollekte</div>

    <p class="date date--sat"><span class="date__day">SAMSTAG</span><span class="date__num">19. NOV. 2016</span></p>
    <p class="venue venue--sat">17.00 Uhr · Wellbach/Rosstal<br>Singsaal Schulhaus Lindenhain</p>

    <p class="date date--sun"><span class="date__day">SONNTAG</span><span class="date__num">20. NOV. 2016</span></p>
    <p class="venue venue--sun">17.00 Uhr · Lindau am Weiher<br>Kornblumsaal</p>

    <p class="website">www.klangfreunde-wellbach.ch</p>
  </article>
</body>
</html>
```